Business card design needed with logo

My business is called QVM Solutions & it is targeted towards mobile equipment maintenance in the Mining and civil industry. My work involves maintenance planning and maintenance management plus also supply tradespeople on a labour hire basis. We can provide from basic shut-down machine rebuild plans to complete rebuild services supply plans and labour to anywhere in Australia. I would like to use the colours Black, Red and Grey, I had done a desgin as attached but doesn't really explain what we do and gears don't embroider well onto shirts.
Updates

I also wanted to see the something replace the gears maybe just making the QVM lettering look a bit different or put together differently 

Hello I have extended the deadline by a few extra days as I would like to update details on the front of card, details below & can be put which ever way looks good;

Neil Patton
Director
0417562938
QVM@mailbrook.com.au
www.qvmsolutions-demo.com.au

On the back of the card I would like to have the below printed;

Capable of providing, but not limited to, across Australia:
- Contract Maintenance Planning.
- Skilled Mobile Maintenance labour hire.
- New machine build specifications. 
- Plant risk assessments and inspections.
- Shut down and rebuild program planning.
- Preventative maintenance tasks, including build of materials lists, creation and review.

Target Market(s)

Contractors and companies that use small and large earthmoving and mining machines

Industry/Entity Type

Business

Contact Information for Business Card

Trading name is QVM Solutions
My name and title is
Neil Patton Director
0417 562 938
QVM@mailbrook.com.au

Logo Text

QVM

```html
<!DOCTYPE html>
<html lang="en">
<head>
<meta charset="utf-8">
<title>QVM Solutions – Business Card</title>
<link rel="stylesheet" href="https://fonts.googleapis.com/css2?family=Nunito+Sans:wght@300;400;700;800&display=swap">
<style>
  :root {
    --stage: #000000;
    --card-grey: #6f6f6f;
    --brand-red: #bb0029;
    --paper: #ffffff;
    --ink: #1e1e1e;
    --font: "Nunito Sans", Arial, sans-serif;
  }
  * { margin: 0; padding: 0; box-sizing: border-box; }
  html, body {
    width: 1200px; height: 1000px; overflow: hidden;
    background: var(--stage);
    font-family: var(--font);
  }
  .stage { position: relative; width: 1200px; height: 1000px; }

  .card {
    position: absolute; top: 81px;
    width: 489px; height: 848px;
    overflow: hidden;
  }
  .card--front { left: 84px; background: var(--card-grey); }
  .card--back { left: 641px; background: var(--paper); }

  .card__disc { position: absolute; left: 0; top: 0; }

  /* Front */
  .brand-name {
    position: absolute; right: 57px; color: var(--paper);
    font-weight: 800; text-align: right; white-space: nowrap;
  }
  .brand-name--primary { top: 112px; font-size: 190px; line-height: 1; letter-spacing: -6px; }
  .brand-name--secondary { top: 285px; font-size: 50px; line-height: 1; letter-spacing: 1px; }

  .contact {
    position: absolute; right: 57px; top: 548px;
    color: var(--paper); text-align: right; white-space: nowrap;
  }
  .contact__name { font-weight: 300; font-size: 36px; line-height: 42px; letter-spacing: 0.5px; }
  .contact__title { font-weight: 700; font-size: 34px; line-height: 42px; }
  .contact__details { margin-top: 28px; font-weight: 300; font-size: 29px; line-height: 36px; }

  /* Back */
  .badge-name {
    position: absolute; right: 14px; color: var(--paper);
    font-weight: 800; text-align: right; line-height: 1;
  }
  .badge-name--primary { top: 37px; font-size: 42px; letter-spacing: -1px; }
  .badge-name--secondary { top: 76px; font-size: 11px; letter-spacing: 0.3px; }

  .services {
    position: absolute; left: 0; top: 144px; width: 100%;
    text-align: center; color: var(--ink);
  }
  .services__heading {
    color: var(--brand-red); font-weight: 800;
    font-size: 25px; line-height: 31px; letter-spacing: 0.3px;
  }
  .services__list { list-style: none; margin-top: 33px; }
  .services__item {
    font-weight: 300; font-size: 25px; line-height: 32px;
    letter-spacing: 0.4px; margin-bottom: 32px;
  }
</style>
</head>
<body>
<main class="stage">

  <section class="card card--front" aria-label="Business card front">
    <svg class="card__disc" width="489" height="848" viewBox="0 0 489 848" aria-hidden="true">
      <circle cx="313" cy="216" r="255" fill="var(--brand-red)"/>
    </svg>
    <div class="brand-name brand-name--primary">QVM</div>
    <div class="brand-name brand-name--secondary">SOLUTIONS</div>

    <div class="contact">
      <p class="contact__name">Neil Patton</p>
      <p class="contact__title">Director</p>
      <p class="contact__details">
        0417562938<br>
        QVM@mailbrook.com.au<br>
        www.qvmsolutions-demo.com.au
      </p>
    </div>
  </section>

  <section class="card card--back" aria-label="Business card back">
    <svg class="card__disc" width="489" height="848" viewBox="0 0 489 848" aria-hidden="true">
      <circle cx="434" cy="60" r="64" fill="var(--brand-red)"/>
    </svg>
    <div class="badge-name badge-name--primary">QVM</div>
    <div class="badge-name badge-name--secondary">SOLUTIONS</div>

    <div class="services">
      <h2 class="services__heading">Capable of providing, but not<br>limited to, across Australia:</h2>
      <ul class="services__list">
        <li class="services__item">- Contract Maintenance Planning</li>
        <li class="services__item">- Skilled Mobile Maintenance<br>labour hire</li>
        <li class="services__item">- New machine build<br>specifications</li>
        <li class="services__item">- Plant risk assessments<br>and inspections</li>
        <li class="services__item">- Shut down and rebuild<br>program planning</li>
        <li class="services__item">- Preventative maintenance tasks,<br>including build of materials lists,<br>creation and review</li>
      </ul>
    </div>
  </section>

</main>
</body>
</html>
```